professional business card design for technology company

We are a small technology consulting firm, specialising in consulting based around Cloud and Managed services. Our colour scheme is yellow, blue and white, as you can see in the logos. Although we are based in melbourne australia, due to the nature of our work, our clients can be located anywhere. We are looking for a clean, professional, positive look - similar to our company logo

Target Market(s)

small business

Industry/Entity Type

Business

Contact Information for Business Card

eye catching, designed to incorporate some level of raised printing. Must contain website address, phone number, name and job title

Requirements
Must have
• Logo (attached) - use of the same colour scheme

```html
<!DOCTYPE html>
<html lang="en">
<head>
<meta charset="utf-8">
<title>Clouvra Business Card</title>
<link rel="stylesheet" href="https://fonts.googleapis.com/css2?family=Montserrat:wght@700&family=Open+Sans:wght@400;700&display=swap">
<style>
  :root {
    --blue: #3aa8df;
    --yellow: #f7dc1c;
    --grey: #58585a;
    --ink: #4a4a4c;
    --white: #ffffff;
    --paper: #fbfbfb;
    --backdrop: #e6e7e9;
  }
  html, body {
    margin: 0;
    width: 1200px;
    height: 863px;
    overflow: hidden;
    background: var(--backdrop);
  }
  .canvas {
    position: relative;
    width: 1200px;
    height: 863px;
  }
  .card {
    position: absolute;
    left: 260px;
    width: 680px;
    height: 388px;
    background: var(--paper);
    overflow: hidden;
    box-shadow: 0 6px 18px rgba(0,0,0,0.18);
    font-family: "Open Sans", Arial, sans-serif;
  }
  .card--front { top: 25px; }
  .card--back { top: 450px; }

  .stripe {
    position: absolute;
    height: 18px;
    background: repeating-linear-gradient(90deg, var(--grey) 0 56px, var(--yellow) 56px 112px);
  }
  .band {
    position: absolute;
    background: var(--blue);
  }
  .corner-tab {
    position: absolute;
    left: 0;
    top: 0;
  }

  .brand {
    position: absolute;
    display: flex;
    align-items: center;
    gap: 14px;
  }
  .brand__dot {
    border-radius: 50%;
    background: var(--blue);
  }
  .brand__name {
    font-family: "Montserrat", Arial, sans-serif;
    font-weight: 700;
    color: var(--ink);
    letter-spacing: -1px;
  }
  .card--front .brand {
    left: 0; right: 0; top: 112px;
    justify-content: center;
  }
  .card--front .brand__dot { width: 58px; height: 58px; }
  .card--front .brand__name { font-size: 64px; }

  .website {
    position: absolute;
    left: 0; right: 0;
    top: 276px;
    text-align: center;
    color: var(--white);
    font-size: 15px;
    letter-spacing: 4px;
  }

  .card--back .brand { left: 36px; top: 120px; }
  .card--back .brand__dot { width: 44px; height: 44px; }
  .card--back .brand__name { font-size: 48px; }

  .person {
    position: absolute;
    left: 56px;
    top: 282px;
    color: var(--white);
  }
  .person__name {
    font-weight: 700;
    font-size: 19px;
    margin: 0;
    letter-spacing: 0.5px;
  }
  .person__title {
    font-size: 14px;
    margin: 2px 0 0;
    letter-spacing: 0.5px;
  }
  .person-marker {
    position: absolute;
    left: 0;
    top: 318px;
    width: 34px;
    height: 30px;
    background: var(--grey);
  }

  .divider-v {
    position: absolute;
    left: 346px;
    top: 112px;
    width: 1px;
    height: 250px;
    background: rgba(255,255,255,0.8);
  }
  .divider-h {
    position: absolute;
    left: 346px;
    top: 112px;
    width: 334px;
    height: 1px;
    background: rgba(255,255,255,0.8);
  }

  .contacts {
    position: absolute;
    left: 364px;
    top: 128px;
    width: 300px;
    margin: 0;
    padding: 0;
    list-style: none;
    color: var(--white);
    font-size: 13.5px;
  }
  .contacts li {
    display: flex;
    align-items: center;
    gap: 10px;
    height: 27px;
    white-space: nowrap;
  }
  .contacts svg {
    width: 15px;
    height: 15px;
    flex: none;
  }
</style>
</head>
<body>
<div class="canvas">

  <section class="card card--front">
    <svg class="corner-tab" width="240" height="20" viewBox="0 0 240 20">
      <path d="M0 0 H240 Q226 0 218 14 Q214 20 206 20 H0 Z" fill="var(--blue)"/>
    </svg>
    <div class="brand">
      <span class="brand__dot"></span>
      <span class="brand__name">Clouvra</span>
    </div>
    <div class="stripe" style="left:0;right:0;top:240px;"></div>
    <div class="band" style="left:0;right:0;top:258px;height:60px;"></div>
    <div class="website">www.clouvraconsult.com</div>
    <div class="stripe" style="left:0;right:0;top:318px;background-position:28px 0;"></div>
    <div class="band" style="left:0;right:0;top:336px;height:52px;"></div>
  </section>

  <section class="card card--back">
    <div class="stripe" style="left:346px;right:0;top:70px;"></div>
    <div class="band" style="left:346px;right:0;top:88px;height:300px;"></div>
    <div class="stripe" style="left:0;width:346px;top:200px;background-position:20px 0;"></div>
    <div class="band" style="left:0;width:346px;top:218px;height:170px;"></div>

    <div class="brand">
      <span class="brand__dot"></span>
      <span class="brand__name">Clouvra</span>
    </div>

    <div class="person-marker"></div>
    <div class="person">
      <p class="person__name">DANIEL REYES</p>
      <p class="person__title">GENERAL MANAGER</p>
    </div>

    <div class="divider-h"></div>
    <div class="divider-v"></div>

    <ul class="contacts">
      <li>
        <svg viewBox="0 0 16 16"><rect x="4" y="1" width="8" height="14" rx="1.5" fill="none" stroke="#fff" stroke-width="1.4"/><circle cx="8" cy="12.5" r="0.9" fill="#fff"/></svg>
        020 555 0148
      </li>
      <li>
        <svg viewBox="0 0 16 16"><path d="M3 2 L6 2 L7 5 L5.5 6.5 Q7 9.5 9.5 10.5 L11 9 L14 10 L14 13 Q13 14.5 11 14 Q4 12 2 5 Q1.5 3 3 2 Z" fill="#fff"/></svg>
        020 555 0172
      </li>
      <li>
        <svg viewBox="0 0 16 16"><rect x="1" y="3" width="14" height="10" rx="1" fill="#fff"/><path d="M1.5 3.8 L8 9 L14.5 3.8" fill="none" stroke="var(--blue)" stroke-width="1.3"/></svg>
        hello@clouvra.com
      </li>
      <li>
        <svg viewBox="0 0 16 16"><circle cx="8" cy="8" r="6.5" fill="none" stroke="#fff" stroke-width="1.3"/><ellipse cx="8" cy="8" rx="3" ry="6.5" fill="none" stroke="#fff" stroke-width="1.1"/><path d="M1.5 8 H14.5" stroke="#fff" stroke-width="1.1"/></svg>
        www.clouvraconsult.com
      </li>
      <li>
        <svg viewBox="0 0 16 16"><path d="M8 15 Q3 9 3 6 A5 5 0 0 1 13 6 Q13 9 8 15 Z" fill="#fff"/><circle cx="8" cy="6" r="1.8" fill="var(--blue)"/></svg>
        Level 4, 27 Harbour Lane, Southport 4215
      </li>
    </ul>
  </section>

</div>
</body>
</html>
```